Halmi Rékas Physiotherapy Business Card Vienna

We need a business card design for a newly created Physiotherapy company based in Vienna Austria.
We seek a simple, modern, minimalist design without too much color variation. The font should look young/fresh, but definitely not childish or so. Since we are a starting Business, we currently haven't got a logo, if you feel like a logo would fit your design, feel free to use one, but it's not necessary.
Target Market(s)
Healthcare, young and elderly people with mobility issues
Industry/Entity Type
Health And Wellness
Contact Information for Business Card
Name: Réka Halmi
Title description: Physiotherapist
Phone num: +43 664 5290 4116
e-mail: reka.praxis@examplemail.net
Colors
Designer to choose colors to be used in the design.
Requirements
Must have
- Final design language must be in German, basically, the Title Description needs to be "Physiotherapeutin" the other details remain as in the English Language.
Nice to have
- Simple, modern, minimalist design
Should not have
- too many colors, Obvious use of a skeleton, skull, spline

```html
<!DOCTYPE html>
<html lang="de">
<head>
<meta charset="utf-8">
<title>Réka Halmi – Visitenkarte</title>
<link rel="stylesheet" href="https://fonts.googleapis.com/css2?family=Archivo+Black&family=Montserrat:wght@300;400;800&display=swap">
<style>
  :root {
    --backdrop-light: #ebecee;
    --backdrop-dark: #c9c9c9;
    --lime: #b5c23a;
    --lime-deep: #a8b62c;
    --lime-pattern: #bccb4a;
    --paper: #ffffff;
    --ink: #1e1e1e;
    --muted-ink: #2a2a2a;
  }
  html, body {
    margin: 0;
    width: 1200px;
    height: 1021px;
    overflow: hidden;
  }
  body {
    background: linear-gradient(160deg, var(--backdrop-light) 0%, var(--backdrop-dark) 100%);
    font-family: "Montserrat", sans-serif;
    position: relative;
  }
  .card {
    position: absolute;
    left: 320px;
    width: 560px;
    height: 320px;
    overflow: hidden;
    box-shadow: 0 3px 8px rgba(0,0,0,0.18);
  }
  /* Back side */
  .card--back {
    top: 140px;
    background: var(--lime);
  }
  .card__pattern {
    position: absolute;
    inset: 0;
    background: linear-gradient(135deg, var(--lime-pattern), var(--lime));
  }
  .title-block {
    position: absolute;
    left: 150px;
    top: 160px;
    transform: translate(-50%, -50%) rotate(-90deg);
    color: var(--paper);
    white-space: nowrap;
    line-height: 1;
  }
  .title-block__strong {
    display: block;
    font-family: "Archivo Black", sans-serif;
    font-size: 34px;
    letter-spacing: 1px;
  }
  .title-block__light {
    display: block;
    font-weight: 300;
    font-size: 28px;
    letter-spacing: 1px;
    margin-top: 4px;
  }
  .brand-name {
    position: absolute;
    right: 60px;
    bottom: 40px;
    color: var(--paper);
    font-weight: 800;
    font-size: 26px;
    letter-spacing: 0.5px;
  }
  /* Front side */
  .card--front {
    top: 510px;
    background: var(--paper);
  }
  .person-name {
    position: absolute;
    left: 28px;
    top: 62px;
    margin: 0;
    font-family: "Archivo Black", sans-serif;
    font-size: 46px;
    line-height: 0.92;
    color: var(--ink);
    letter-spacing: 0.5px;
  }
  .role-band {
    position: absolute;
    left: 24px;
    right: 0;
    top: 160px;
    height: 30px;
    background: var(--lime-deep);
  }
  .role-band__text {
    position: absolute;
    left: 8px;
    top: 1px;
    color: var(--paper);
    font-size: 24px;
    font-weight: 400;
    line-height: 28px;
  }
  .contact {
    position: absolute;
    top: 206px;
    left: 24px;
    right: 24px;
    display: flex;
    gap: 32px;
    font-size: 15px;
    color: var(--muted-ink);
  }
  .contact__item {
    display: flex;
    align-items: center;
    gap: 6px;
  }
  .contact__icon { width: 14px; height: 14px; }
  .footer-stripe {
    position: absolute;
    left: 0;
    right: 0;
    top: 252px;
    height: 26px;
    background: var(--lime-deep);
  }
</style>
</head>
<body>

  <section class="card card--back">
    <div class="card__pattern" role="img" aria-label="Dezentes geometrisches Muster in Grüntönen"></div>
    <div class="title-block">
      <span class="title-block__strong">PHYSIO</span>
      <span class="title-block__light">THERAPEUTIN</span>
    </div>
    <div class="brand-name">Réka Halmi</div>
  </section>

  <section class="card card--front">
    <h1 class="person-name">RÉKA<br>HALMI</h1>
    <div class="role-band"><span class="role-band__text">Physiotherapeutin</span></div>
    <div class="contact">
      <span class="contact__item">
        <svg class="contact__icon" viewBox="0 0 24 24" aria-hidden="true">
          <path fill="#a8b62c" d="M6.6 10.8a15 15 0 0 0 6.6 6.6l2.2-2.2a1 1 0 0 1 1-.25 11.4 11.4 0 0 0 3.6.57 1 1 0 0 1 1 1V20a1 1 0 0 1-1 1A17 17 0 0 1 3 4a1 1 0 0 1 1-1h3.5a1 1 0 0 1 1 1c0 1.25.2 2.45.57 3.57a1 1 0 0 1-.25 1z"/>
        </svg>
        +43 664 5290 4116
      </span>
      <span class="contact__item">
        <svg class="contact__icon" viewBox="0 0 24 24" aria-hidden="true">
          <rect x="2" y="5" width="20" height="14" fill="none" stroke="#a8b62c" stroke-width="2.5"/>
          <path d="M2 5l10 8 10-8" fill="none" stroke="#a8b62c" stroke-width="2.5"/>
        </svg>
        reka.praxis@examplemail.net
      </span>
    </div>
    <div class="footer-stripe"></div>
  </section>

</body>
</html>
```